Modern Business Card

Modern professional business card with more than just logo and demographic info. Something memorable.

We are a trendy/modern chiropractic group with an emphasis on neurology, hence the minimalist-type brain logo. We want to convey that modern and technical aspect with professionalism and the elite nature of our practice environment.

```html
<!DOCTYPE html>
<html lang="en">
<head>
<meta charset="utf-8">
<title>Meridian Chiropractic – Business Card</title>
<link rel="stylesheet" href="https://fonts.googleapis.com/css2?family=Libre+Baskerville&family=Lato:wght@400;700&display=swap">
<style>
  :root {
    --bg: #e4e2e3;
    --card: #ffffff;
    --brand-blue: #4a82c5;
    --ink: #1c1c1c;
    --ink-soft: #3a3a3a;
    --ghost: #f0f1f3;
    --shadow: rgba(0,0,0,0.18);
  }
  * { box-sizing: border-box; margin: 0; padding: 0; }
  html, body { width: 1200px; height: 1200px; overflow: hidden; }
  body {
    background: var(--bg);
    font-family: "Lato", Arial, sans-serif;
    position: relative;
  }
  .card {
    position: absolute;
    left: 220px;
    width: 760px;
    height: 434px;
    background: var(--card);
    border-radius: 32px;
    box-shadow: 0 14px 30px var(--shadow);
    overflow: hidden;
  }
  .card--front { top: 120px; }
  .card--back { top: 646px; }

  .brand {
    display: flex;
    align-items: center;
    gap: 18px;
    font-family: "Libre Baskerville", Georgia, serif;
    color: var(--ink);
    text-transform: uppercase;
    line-height: 1;
  }
  .brand__dot {
    background: var(--brand-blue);
    border-radius: 50%;
    flex: none;
  }
  .card--front .brand {
    position: absolute;
    left: 50%; top: 50%;
    transform: translate(-50%, -50%);
    font-size: 40px;
    letter-spacing: 2px;
    white-space: nowrap;
  }
  .card--front .brand__dot { width: 64px; height: 64px; }

  .card--back .brand {
    position: absolute;
    right: 60px; top: 62px;
    font-size: 26px;
    letter-spacing: 1.5px;
    white-space: nowrap;
  }
  .card--back .brand__dot { width: 40px; height: 40px; }

  .ghost-shape {
    position: absolute;
    right: -90px; bottom: -110px;
    width: 360px; height: 360px;
    border-radius: 50%;
    background: var(--ghost);
  }

  .person {
    position: absolute;
    left: 60px; bottom: 60px;
  }
  .person__name {
    font-size: 34px;
    font-weight: 700;
    color: var(--brand-blue);
    letter-spacing: 0.5px;
  }
  .person__role {
    font-size: 17px;
    color: var(--ink-soft);
    margin-bottom: 22px;
  }
  .contact { list-style: none; }
  .contact__item {
    display: flex;
    align-items: center;
    gap: 14px;
    font-size: 18px;
    color: var(--ink-soft);
    margin-top: 7px;
  }
  .contact__item svg { width: 20px; height: 20px; fill: var(--brand-blue); flex: none; }
  .contact__accent { color: var(--brand-blue); }
</style>
</head>
<body>

<section class="card card--front" aria-label="Card front">
  <div class="brand">
    <span class="brand__dot"></span>
    <span class="brand__name">Meridian Chiropractic</span>
  </div>
</section>

<section class="card card--back" aria-label="Card back">
  <div class="ghost-shape"></div>
  <div class="brand">
    <span class="brand__dot"></span>
    <span class="brand__name">Meridian Chiropractic</span>
  </div>

  <div class="person">
    <h1 class="person__name">Daniel Reyes</h1>
    <p class="person__role">neurologist</p>
    <ul class="contact">
      <li class="contact__item">
        <svg viewBox="0 0 24 24"><path d="M6.6 10.8a15.1 15.1 0 0 0 6.6 6.6l2.2-2.2c.3-.3.7-.4 1-.2 1.1.4 2.3.6 3.6.6.6 0 1 .4 1 1V20c0 .6-.4 1-1 1A17 17 0 0 1 3 4c0-.6.4-1 1-1h3.5c.6 0 1 .4 1 1 0 1.3.2 2.5.6 3.6.1.3 0 .7-.2 1z"/></svg>
        1-555-014-2276
      </li>
      <li class="contact__item">
        <svg viewBox="0 0 24 24"><path d="M12 2a10 10 0 1 0 0 20 10 10 0 0 0 0-20zm6.9 6h-3a15.6 15.6 0 0 0-1.3-3.6A8 8 0 0 1 18.9 8zM12 4c.8 1.2 1.5 2.5 1.9 4h-3.8c.4-1.5 1.1-2.8 1.9-4zM4.3 14a8.2 8.2 0 0 1 0-4h3.4a16 16 0 0 0 0 4zm.8 2h3a15.6 15.6 0 0 0 1.3 3.6A8 8 0 0 1 5.1 16zm3-8h-3a8 8 0 0 1 4.3-3.6C8.8 5.5 8.4 6.7 8.1 8zM12 20c-.8-1.2-1.5-2.5-1.9-4h3.8c-.4 1.5-1.1 2.8-1.9 4zm2.3-6H9.7a14.7 14.7 0 0 1 0-4h4.6a14.7 14.7 0 0 1 0 4zm.3 5.6c.6-1.1 1-2.3 1.3-3.6h3a8 8 0 0 1-4.3 3.6zm1.7-5.6a16 16 0 0 0 0-4h3.4a8.2 8.2 0 0 1 0 4z"/></svg>
        <span>daniel@<span class="contact__accent">meridianchiropractic</span>.com</span>
      </li>
      <li class="contact__item">
        <svg viewBox="0 0 24 24"><path d="M3 5h18c.6 0 1 .4 1 1v12c0 .6-.4 1-1 1H3c-.6 0-1-.4-1-1V6c0-.6.4-1 1-1zm1 2.2V17h16V7.2l-8 5.3z M4.5 7l7.5 5 7.5-5z"/></svg>
        <span>www.<span class="contact__accent">meridianchiropractic</span>.com</span>
      </li>
      <li class="contact__item">
        <svg viewBox="0 0 24 24"><path d="M12 2a7 7 0 0 0-7 7c0 5 7 13 7 13s7-8 7-13a7 7 0 0 0-7-7zm0 9.5A2.5 2.5 0 1 1 12 6.5a2.5 2.5 0 0 1 0 5z"/></svg>
        Lakeview City, Northland
      </li>
    </ul>
  </div>
</section>

</body>
</html>
```